Keystone Tenancy Hour podcast postcard

I've launched a podcast about apartment investing, ownership and management which is newly up on quorl and brevano. I want to create a postcard that I can mail to my client base to get them to subscribe

```html
<!DOCTYPE html>
<html lang="en">
<head>
<meta charset="utf-8">
<title>Keystone Tenancy Hour Podcast Postcard</title>
<link href="https://fonts.googleapis.com/css2?family=Anton&family=Oswald:wght@300;500&display=swap" rel="stylesheet">
<style>
  :root {
    --purple: #4a3f94;
    --purple-deep: #3d3380;
    --lavender: #e6e4f2;
    --orange: #ee7d14;
    --peach: #fbe3cf;
    --ink: #1d1d1f;
    --white: #ffffff;
    --stage: #ececec;
    --sky: #3fa6b5;
    --sand: #e9d2a0;
  }
  * { box-sizing: border-box; margin: 0; padding: 0; }
  html, body { width: 1200px; height: 900px; overflow: hidden; background: var(--stage); }
  .stage { position: relative; width: 1200px; height: 900px; }

  .card {
    position: absolute; width: 560px; height: 374px; background: var(--white);
    overflow: hidden; box-shadow: 0 6px 18px rgba(0,0,0,.18);
  }
  .card--front { left: 30px; top: 263px; }
  .card--back  { left: 610px; top: 263px; }
  .card__bg { position: absolute; inset: 0; }

  .cover {
    position: absolute; background: var(--white); padding: 8px;
    box-shadow: 0 4px 10px rgba(0,0,0,.25);
  }
  .cover__art {
    width: 100%; height: 100%;
    background: linear-gradient(200deg, var(--sky) 0%, #5bb6bf 45%, var(--sand) 70%, #d8b777 100%);
  }

  .mark { position: absolute; border-radius: 50%; border: 4px solid var(--white); }

  .title {
    position: absolute; font-family: "Anton", sans-serif; color: var(--white);
    line-height: 1.02; letter-spacing: .5px; text-transform: uppercase;
  }
  .title__sub {
    display: block; font-family: "Oswald", sans-serif; font-weight: 300; letter-spacing: 0;
  }

  .cta {
    position: absolute; font-family: "Anton", sans-serif; color: var(--orange);
    text-transform: uppercase; line-height: 1;
  }

  .platforms {
    position: absolute; display: flex; align-items: center; gap: 10px;
    font-family: "Oswald", sans-serif; font-weight: 500; color: var(--ink);
    text-transform: uppercase;
  }
  .platform { display: flex; align-items: center; gap: 4px; text-transform: none; }
  .platform__dot { width: 10px; height: 10px; border-radius: 50%; background: var(--ink); }

  /* front */
  .card--front .cover { left: 22px; top: 92px; width: 228px; height: 228px; transform: rotate(-6deg); }
  .card--front .mark { left: 398px; top: 16px; width: 44px; height: 44px; }
  .card--front .title { left: 290px; top: 70px; width: 260px; text-align: center; font-size: 40px; }
  .card--front .title__sub { font-size: 30px; margin-top: 4px; }
  .card--front .cta { right: 22px; top: 258px; font-size: 37px; text-align: right; }
  .card--front .platforms { right: 22px; top: 334px; font-size: 15px; }

  /* back */
  .card--back .mark { left: 16px; top: 26px; width: 44px; height: 44px; }
  .card--back .title { left: 72px; top: 16px; font-size: 31px; }
  .card--back .title__sub { font-size: 24px; margin-top: 2px; }
  .card--back .cover { left: 78px; top: 128px; width: 170px; height: 170px; transform: rotate(-3deg); }
  .card--back .cta { left: 18px; top: 322px; font-size: 15px; }
  .card--back .platforms { left: 130px; top: 328px; font-size: 13px; }
  .stamp-box {
    position: absolute; left: 478px; top: 12px; width: 66px; height: 66px;
    border: 3px solid #d9d9d9;
  }
  .address-line {
    position: absolute; left: 340px; width: 200px; border-top: 1px dashed #d4d4d4;
  }
</style>
</head>
<body>
<main class="stage">

  <section class="card card--front" aria-label="Postcard front">
    <svg class="card__bg" viewBox="0 0 560 374" preserveAspectRatio="none" aria-hidden="true">
      <defs>
        <linearGradient id="peachFade" x1="0" y1="0" x2="1" y2="0">
          <stop offset="0" stop-color="#fbe3cf"/>
          <stop offset="1" stop-color="#ffffff"/>
        </linearGradient>
      </defs>
      <polygon points="0,250 560,300 560,374 0,374" fill="url(#peachFade)"/>
      <polygon points="0,90 280,185 0,175" fill="#e6e4f2"/>
      <polygon points="0,0 560,0 560,182 418,245 270,182 0,90" fill="#4a3f94"/>
      <rect x="60" y="-40" width="120" height="160" rx="22" fill="#3d3380" opacity=".45" transform="rotate(18 120 40)"/>
      <rect x="470" y="-30" width="110" height="170" rx="22" fill="#3d3380" opacity=".45" transform="rotate(-12 525 55)"/>
      <polygon points="0,366 560,356 560,362 0,374" fill="#ee7d14"/>
    </svg>

    <figure class="cover">
      <div class="cover__art" role="img" aria-label="Podcast cover art: apartment building against a blue sky with the show name"></div>
    </figure>

    <span class="mark" aria-hidden="true"></span>
    <h1 class="title">Keystone<br>Tenancy Hour<span class="title__sub">Podcast</span></h1>
    <p class="cta">Follow and<br>Subscribe</p>
    <p class="platforms">Available in
      <span class="platform"><span class="platform__dot"></span>brevano</span>
      <span class="platform">quorl</span>
    </p>
  </section>

  <section class="card card--back" aria-label="Postcard back">
    <svg class="card__bg" viewBox="0 0 560 374" preserveAspectRatio="none" aria-hidden="true">
      <rect x="0" y="0" width="320" height="374" rx="0" fill="#e6e4f2"/>
      <polygon points="0,0 320,0 320,135 200,158 0,130" fill="#4a3f94"/>
      <rect x="150" y="-30" width="100" height="150" rx="20" fill="#3d3380" opacity=".45" transform="rotate(15 200 45)"/>
      <polygon points="0,260 320,300 320,374 0,374" fill="#ffffff"/>
    </svg>

    <span class="mark" aria-hidden="true"></span>
    <h2 class="title">Keystone<br>Tenancy Hour<span class="title__sub">Podcast</span></h2>

    <figure class="cover">
      <div class="cover__art" role="img" aria-label="Podcast cover art: apartment building against a blue sky with the show name"></div>
    </figure>

    <p class="cta">Follow and<br>Subscribe</p>
    <p class="platforms">Available in
      <span class="platform"><span class="platform__dot"></span>brevano</span>
      <span class="platform">quorl</span>
    </p>

    <div class="stamp-box" aria-hidden="true"></div>
    <div class="address-line" style="top:200px"></div>
    <div class="address-line" style="top:235px"></div>
    <div class="address-line" style="top:270px"></div>
    <div class="address-line" style="top:305px"></div>
  </section>

</main>
</body>
</html>
```